Waste Oil Filter collection & disposal

Basically I need a 1 page website for the business called Canister Recovery Works.
We are a environmental service provider and we collect and dispose of waste oil filters to protect the environment from hazardous waste oil products.

This is the link to our current website: www.canisterrecovery.co.nz

we want it to look fresh and better than our current website. we may potentially look at getting a new logo designed and are open to ideas/designs if you have any.

Industry/Entity Type

Business

Logo Text

Canister Recovery Works

Number of Pages Required

1 page

Requirements
Must have
• same colours as current website.
• description of what service we provide please refer to leaflet attached

```html
<!DOCTYPE html>
<html lang="en">
<head>
<meta charset="utf-8">
<title>Canister Recovery Works Ltd</title>
<link href="https://fonts.googleapis.com/css2?family=Montserrat:wght@400;500;600;700&display=swap" rel="stylesheet">
<style>
:root{
  --green:#1f9a26;
  --green-bright:#2fb533;
  --green-dark:#17871d;
  --ink:#333;
  --muted:#666;
  --light:#f4f4f4;
  --dark:#262626;
  --white:#fff;
  --grey-circle:#9a9a9a;
}
*{box-sizing:border-box;margin:0;padding:0}
html,body{width:1200px;height:2432px;overflow:hidden}
body{position:relative;font-family:'Montserrat',sans-serif;color:var(--ink);background:var(--white)}

/* header */
.site-header{position:absolute;left:0;top:0;width:1200px;height:94px;background:var(--light)}
.brand-dot{position:absolute;border-radius:50%;background:var(--green)}
.brand-name{position:absolute;font-weight:600;font-size:18px;color:var(--dark);letter-spacing:.3px;white-space:nowrap}
.brand-tag{position:absolute;font-size:12px;letter-spacing:4px;color:var(--muted);text-transform:uppercase;white-space:nowrap}
.phone{position:absolute;display:flex;align-items:center;gap:12px;font-size:21px;color:var(--ink);letter-spacing:1px;white-space:nowrap}
.social{position:absolute;width:26px;height:26px;border-radius:50%}
.social.one{background:var(--green-bright)}
.social.two{background:var(--grey-circle)}

/* hero */
.hero{position:absolute;left:0;top:94px;width:1200px;height:482px;background:radial-gradient(ellipse at 50% 35%,#6d7d88 0%,#3e4a54 45%,#1d242b 100%)}
.hero-title{position:absolute;left:170px;top:211px;width:860px;height:56px;background:var(--green);color:var(--white);font-weight:700;font-size:30px;letter-spacing:2.5px;display:flex;align-items:center;justify-content:center;box-shadow:0 3px 8px rgba(0,0,0,.4)}

/* about */
.section-title{position:absolute;font-size:30px;font-weight:500;letter-spacing:1.5px;color:var(--dark)}
.rule{position:absolute;height:2px;width:38px;background:var(--green)}
.about-lead{position:absolute;left:186px;top:742px;width:470px;font-size:14.5px;font-weight:600;line-height:1.45;color:var(--green)}
.about-body{position:absolute;left:186px;top:808px;width:470px;font-size:13px;line-height:1.6;color:var(--muted)}
.about-photo{position:absolute;left:684px;top:622px;width:336px;height:316px;border-radius:50%;background:radial-gradient(circle at 50% 45%,#4fae6a 0%,#2f7a4e 45%,#4a4f52 100%);box-shadow:0 0 0 8px #e6e6e6}

/* process */
.process{position:absolute;left:0;top:981px;width:1200px;height:532px;background:linear-gradient(180deg,var(--green-bright),var(--green-dark));color:var(--white)}
.process .section-title{color:var(--white);left:0;width:1200px;text-align:center;top:56px}
.process .rule{background:var(--white);left:581px;top:102px}
.process-intro{position:absolute;left:0;width:1200px;top:118px;text-align:center;font-size:13px}
.step{position:absolute;top:243px;width:180px;text-align:center}
.step-num{margin:0 auto;width:52px;height:52px;border-radius:50%;background:rgba(40,70,40,.35);display:flex;align-items:center;justify-content:center;font-size:24px;font-weight:600;color:rgba(255,255,255,.55)}
.step-label{margin-top:18px;font-size:16px;font-weight:600;letter-spacing:1px;line-height:1.4}
.process-note{position:absolute;left:0;width:1200px;top:457px;text-align:center;font-size:13px}
.process-note strong{color:#0d5e12}

/* service */
.service-photo{position:absolute;left:100px;top:1573px;width:476px;height:332px;background:linear-gradient(135deg,#5d6d6a 0%,#2d7568 40%,#4b5053 100%);box-shadow:0 2px 10px rgba(0,0,0,.35)}
.service-title{position:absolute;left:613px;top:1606px;width:500px;font-size:21px;font-weight:500;line-height:1.5;color:var(--dark)}
.service-list{position:absolute;left:613px;top:1718px;width:470px;list-style:none}
.service-list li{display:flex;gap:10px;font-size:13px;line-height:1.45;color:var(--muted);margin-bottom:14px}
.service-list svg{flex:none;margin-top:2px}

/* pricing */
.pricing{position:absolute;left:0;top:1967px;width:1200px;height:174px;background:linear-gradient(180deg,#2e2e2e,#1c1c1c)}
.price{position:absolute;top:56px;width:320px;text-align:center;color:var(--white)}
.price-amount{font-size:30px;font-weight:600;color:var(--green-bright);letter-spacing:1.5px}
.price-amount small{font-size:15px;color:var(--white);margin-right:4px}
.price-label{margin-top:4px;font-size:16px;font-weight:500;letter-spacing:1px}

/* contact */
.contact{position:absolute;left:0;top:2141px;width:1200px;height:256px;background:#e3e3e3}
.contact-title{position:absolute;left:97px;top:54px;font-size:16px;font-weight:600;color:var(--green);letter-spacing:1px}
.field{position:absolute;background:var(--white);border:1px solid #ddd;font-size:13px;color:#999;padding:8px 14px}
.send{position:absolute;left:556px;top:129px;width:31px;height:65px;background:var(--green);display:flex;align-items:center;justify-content:center}

.site-footer{position:absolute;left:0;top:2397px;width:1200px;height:35px;background:var(--green);color:var(--white);font-size:13px;display:flex;align-items:center;justify-content:center}
</style>
</head>
<body>

<header class="site-header">
  <div class="brand-dot" style="left:97px;top:16px;width:62px;height:62px"></div>
  <div class="brand-name" style="left:191px;top:24px">CANISTER RECOVERY WORKS LTD</div>
  <div class="brand-tag" style="left:191px;top:52px">Clean filters, cleaner land</div>
  <div class="phone" style="left:752px;top:32px">
    <svg width="26" height="26" viewBox="0 0 24 24"><path fill="#2fb533" d="M6.6 10.8a15.1 15.1 0 0 0 6.6 6.6l2.2-2.2c.3-.3.7-.4 1-.2 1.1.4 2.3.6 3.6.6.6 0 1 .4 1 1V20c0 .6-.4 1-1 1A17 17 0 0 1 3 4c0-.6.4-1 1-1h3.5c.6 0 1 .4 1 1 0 1.3.2 2.5.6 3.6.1.3 0 .7-.2 1z"/></svg>
    06 555 0142
  </div>
  <div class="social one" style="left:1034px;top:34px"></div>
  <div class="social two" style="left:1066px;top:34px"></div>
</header>

<section class="hero" role="img" aria-label="Close-up photograph of stacked used oil filter canisters">
  <h1 class="hero-title">OIL FILTER COLLECTION &amp; DISPOSAL SERVICE</h1>
</section>

<section class="about">
  <h2 class="section-title" style="left:186px;top:680px">ABOUT US</h2>
  <div class="rule" style="left:186px;top:727px;width:30px"></div>
  <p class="about-lead">Canister Recovery Works Ltd specialize in the collection &amp; disposal of oil / fuel filters, servicing the lower north island on a monthly cycle.</p>
  <p class="about-body">We offer a cost effective environmentally friendly system for the collection and disposal of waste oil filters helping minimise contamination of landfills keeping your industry compliant.</p>
  <div class="about-photo" role="img" aria-label="Circular collage of the collection truck and the filter processing plant"></div>
</section>

<section class="process">
  <h2 class="section-title">OUR PROCESS</h2>
  <div class="rule"></div>
  <p class="process-intro">Filters are collected and transported back to the processing plant. At the processing plant they are:</p>
  <div class="step" style="left:80px"><div class="step-num">1</div><div class="step-label">DRAINED</div></div>
  <div class="step" style="left:252px"><div class="step-num">2</div><div class="step-label">SORTED</div></div>
  <div class="step" style="left:424px"><div class="step-num">3</div><div class="step-label">DRAINED<br>AGAIN</div></div>
  <div class="step" style="left:596px"><div class="step-num">4</div><div class="step-label">CRUSHED INTO<br>BRICKS</div></div>
  <div class="step" style="left:766px"><div class="step-num">5</div><div class="step-label">DRAINED A<br>THIRD TIME</div></div>
  <div class="step" style="left:938px"><div class="step-num">6</div><div class="step-label">STACKED<br>READY FOR<br>MATAL<br>RECYCLING</div></div>
  <p class="process-note"><strong>What Happens to The Oil:</strong> All residual oil is collected into our tank and then recycled. Currently we are processing over 2,000 litres of oil a month.</p>
</section>

<section class="service">
  <div class="service-photo" role="img" aria-label="Photograph of the filter crushing line inside the processing plant"></div>
  <h2 class="service-title">Canister Recovery Works Ltd service the Lower North Island and specialise in the collection &amp; disposal of oil &amp; fuel filters</h2>
  <div class="rule" style="left:613px;top:1702px"></div>
  <ul class="service-list">
    <li><svg width="14" height="14" viewBox="0 0 14 14"><path fill="#1f9a26" d="M0 5h8V1l6 6-6 6V9H0z"/></svg>We are passionate about doing our bit in keeping New Zealand Clean and Green</li>
    <li><svg width="14" height="14" viewBox="0 0 14 14"><path fill="#1f9a26" d="M0 5h8V1l6 6-6 6V9H0z"/></svg>Our processes are environmentally friendly and minimise the contamination of landfills.</li>
    <li><svg width="14" height="14" viewBox="0 0 14 14"><path fill="#1f9a26" d="M0 5h8V1l6 6-6 6V9H0z"/></svg>We offer a cost effective system for the collection and disposal of waste oil filters</li>
    <li><svg width="14" height="14" viewBox="0 0 14 14"><path fill="#1f9a26" d="M0 5h8V1l6 6-6 6V9H0z"/></svg>We keep your industry compliant</li>
  </ul>
</section>

<section class="pricing">
  <div class="price" style="left:83px"><div class="price-amount"><small>$</small>65.00</div><div class="price-label">MONTHLY BIN COLLECTION</div></div>
  <div class="price" style="left:440px"><div class="price-amount"><small>$</small>35.00 ea</div><div class="price-label">ADDITIONAL BINS</div></div>
  <div class="price" style="left:780px"><div class="price-amount"><small>$</small>$85.00</div><div class="price-label">ACCOUNT SET UP FEE</div></div>
</section>

<section class="contact">
  <h2 class="contact-title">CONTACT US</h2>
  <div class="field" style="left:100px;top:81px;width:231px;height:33px">Name</div>
  <div class="field" style="left:353px;top:81px;width:234px;height:33px">Email</div>
  <div class="field" style="left:100px;top:129px;width:456px;height:65px">Message</div>
  <div class="send"><svg width="16" height="16" viewBox="0 0 16 16"><path fill="#fff" d="M15 1 1 7l5 2 2 6 7-14zM6 9l7-7-5 10z"/></svg></div>
  <div class="brand-dot" style="left:697px;top:77px;width:57px;height:57px"></div>
  <div class="brand-name" style="left:775px;top:82px">CANISTER RECOVERY WORKS LTD</div>
  <div class="brand-tag" style="left:775px;top:110px">Clean filters, cleaner land</div>
  <div class="phone" style="left:766px;top:150px">
    <svg width="26" height="26" viewBox="0 0 24 24"><path fill="#2fb533" d="M6.6 10.8a15.1 15.1 0 0 0 6.6 6.6l2.2-2.2c.3-.3.7-.4 1-.2 1.1.4 2.3.6 3.6.6.6 0 1 .4 1 1V20c0 .6-.4 1-1 1A17 17 0 0 1 3 4c0-.6.4-1 1-1h3.5c.6 0 1 .4 1 1 0 1.3.2 2.5.6 3.6.1.3 0 .7-.2 1z"/></svg>
    06 555 0142
  </div>
  <div class="social one" style="left:1006px;top:152px"></div>
  <div class="social two" style="left:1038px;top:152px"></div>
</section>

<footer class="site-footer">© 2017 | All Rights Reserved</footer>

</body>
</html>
```